KSI Business Card

Please create a creative design for a business card using the new theme from the Logo & website. This company's main focus is food manufacturing building construction. Please integrate the new logo attached.

Please use the following information for the demo card:

Kelvane Systems, Inc.
Doug Farnham
dfarnham@kelvanesys.example
Cell: 630-555-0193
218 Harbison Ln
Brackenfield, WN 60194

See pictures and more information on the website.

www.kelvanesys.example

```html
<!DOCTYPE html>
<html lang="en">
<head>
<meta charset="utf-8">
<title>KSI Business Card</title>
<link href="https://fonts.googleapis.com/css2?family=Michroma&family=Montserrat:wght@400;600&display=swap" rel="stylesheet">
<style>
  :root {
    --backdrop: #3a3a3c;
    --backdrop-edge: #262628;
    --card: #161618;
    --card-edge: #1e1e21;
    --brand-blue: #3d86d6;
    --text-light: #e9edf2;
    --emblem-tint: rgba(70, 100, 130, 0.35);
  }
  html, body {
    margin: 0;
    padding: 0;
    width: 1200px;
    height: 901px;
    overflow: hidden;
  }
  body {
    background: radial-gradient(ellipse at 55% 35%, var(--backdrop) 0%, var(--backdrop-edge) 100%);
    font-family: "Montserrat", Arial, sans-serif;
    position: relative;
  }
  .card {
    position: absolute;
    left: 270px;
    width: 660px;
    height: 377px;
    background: linear-gradient(160deg, var(--card-edge), var(--card));
    box-shadow: 0 18px 40px rgba(0,0,0,0.55);
    overflow: hidden;
  }
  .card-front { top: 50px; }
  .card-back { top: 470px; }

  .front-brand {
    position: absolute;
    inset: 0;
    display: flex;
    align-items: center;
    justify-content: center;
    gap: 14px;
  }
  .brand-name {
    font-family: "Montserrat", Arial, sans-serif;
    font-weight: 600;
    color: var(--brand-blue);
    letter-spacing: 0.02em;
    margin: 0;
  }
  .front-brand .brand-name { font-size: 36px; }
  .brand-dot {
    width: 14px;
    height: 14px;
    border-radius: 50%;
    background: var(--brand-blue);
  }

  .back-brand {
    position: absolute;
    left: 48px;
    top: 40px;
  }
  .back-brand .brand-name { font-size: 21px; }

  .emblem-watermark {
    position: absolute;
    right: 20px;
    top: 80px;
    width: 330px;
    height: 330px;
    border-radius: 50%;
    background: radial-gradient(circle, var(--emblem-tint) 0%, rgba(70,100,130,0) 70%);
  }

  .contact {
    position: absolute;
    left: 48px;
    top: 200px;
  }
  .person-name {
    font-family: "Michroma", "Arial Black", sans-serif;
    color: var(--brand-blue);
    font-size: 22px;
    letter-spacing: 0.14em;
    margin: 0 0 14px 20px;
    text-transform: uppercase;
  }
  .contact-list {
    list-style: none;
    margin: 0 0 6px 20px;
    padding: 0;
    font-size: 15px;
    line-height: 1.5;
    color: var(--text-light);
  }
  .contact-label {
    color: var(--brand-blue);
    display: inline-block;
    width: 32px;
  }
  .address {
    margin: 0;
    font-size: 15px;
    color: var(--text-light);
  }
</style>
</head>
<body>
  <section class="card card-front" aria-label="Card front">
    <div class="front-brand">
      <span class="brand-dot"></span>
      <h1 class="brand-name">Kelvane Systems, Inc.</h1>
    </div>
  </section>

  <section class="card card-back" aria-label="Card back">
    <div class="back-brand">
      <p class="brand-name">Kelvane Systems, Inc.</p>
    </div>
    <div class="emblem-watermark" role="img" aria-label="Large faint brand emblem area"></div>
    <div class="contact">
      <h2 class="person-name">Doug Farnham</h2>
      <ul class="contact-list">
        <li><span class="contact-label">P :</span>630-555-0193</li>
        <li><span class="contact-label">E :</span>dfarnham@kelvanesys.example</li>
        <li><span class="contact-label">W :</span>www.kelvanesys.example</li>
      </ul>
      <p class="address">218 Harbison Ln, Brackenfield, WN 60194</p>
    </div>
  </section>
</body>
</html>
```